Mens Jewellery Homepage - Modern, Stylish Mens Ring Brand - Homepage

Project Overview: TorvikLoops.com is a men's accessories brand specializing in high-quality mens rings.

The objective of this redesign is to create a modern, visually appealing homepage that is easy to navigate, showcases a wide range of rings, highlights personalization options, and builds trust with customers.

The new design should make a strong impression while reflecting the brand's premium quality and commitment to craftsmanship.

The focus will be on a sleek aesthetic that aligns with the tastes of men shopping for wedding bands, engagement rings, or fashion accessories.

Objectives:

Modern and Sleek Aesthetic:

A clean, minimalist design that emphasizes high-quality product imagery and thoughtful use of space.
Contemporary color palette that conveys elegance and sophistication, with accents that highlight key elements without overwhelming the user.

Consistent and easy-to-read typography that reflects the brand’s modern and masculine identity.

Showcasing Products:
Hero Section: A image to show off 3 or 4 ring designs that could be used for weddings or fashion.

Product Highlights: Below the hero banner, showcase product categories by color (see current website for colors)

Featured Products: Display a selection of “Top Rated” or “Customer Favorites” rings to help guide users toward popular choices.

Personalization Section:
A dedicated section promoting the ability to personalize rings, emphasizing features like engraving with names, dates, or special messages.
Include lifestyle images of personalized rings to inspire customers and give them an idea of what’s possible.
Use callouts such as “Make It Yours” or “Personalize Your Ring” to encourage users to explore the customization options available for each product.

Building Trust:

A space to show 5 or 6 testimonials and other trust elements

Symbols / text to show

free delivery
free returns
every ring stock
fast delivery
customer images (from reviews)

Driving Conversions:
Include a prominent call-to-action (CTA) button in the hero section with text like “Shop Now” or “Discover Our Collections.”

User Experience:
Fast, easy-to-navigate layout with simple and intuitive categories. Product categories and main sections should be clearly visible and easy to access without overwhelming the user.
Design the homepage to feel cohesive and uncluttered, with a logical flow from product discovery to personalization and checkout.

Visual Elements and Imagery:
Use ring images from our site, but add backgrounds etc to make the image on the homepage more interesting.

Personalization Options: Use visual representations (like ring mockups) showing where personalization options (such as engravings) would appear on the product.

I like (and would like to see some different designs from our current design)
Brix.com for design
stoutcircles.com

Target Market(s)

Men - 20 to 35

Number of Pages Required

1 page

Requirements
Must have
• Easy navigation, Trust, Modern, Clean,
Nice to have
• Would like to see Different designs like Brix.com - StoutCircles.com

```html
<!DOCTYPE html>
<html lang="en">
<head>
<meta charset="utf-8">
<title>TorvikLoops – Homepage Concepts</title>
<link href="https://fonts.googleapis.com/css2?family=Poppins:wght@400;500;600;700&display=swap" rel="stylesheet">
<style>
:root{
  --teal:#0e807b;
  --teal-light:#7fc4c0;
  --ink:#111;
  --muted:#777;
  --board:#222;
  --dark:#262626;
  --blue:#2a87cc;
  --blush:#fbe6dd;
  --grey:#f2f2f2;
  --white:#fff;
}
*{box-sizing:border-box;margin:0;padding:0}
html,body{width:988px;height:1200px;overflow:hidden;background:var(--board);font-family:"Poppins",sans-serif;color:var(--ink)}
.board{position:absolute;left:0;top:0;width:1736px;height:2108px;transform:scale(.5691);transform-origin:0 0;background:var(--board)}
.col{position:absolute;top:14px;width:566px;background:var(--white);overflow:hidden}
.col-a{left:13px}.col-b{left:585px}.col-c{left:1157px}

.topbar{height:22px;background:var(--teal);display:flex;justify-content:center;align-items:center;gap:28px;color:#fff;font-size:7px}
.topbar span{display:flex;align-items:center;gap:8px}
.topbar span::before{content:"";width:11px;height:11px;border-radius:50%;background:#fff}
.nav{height:46px;display:flex;align-items:center;padding:0 18px;gap:18px;font-size:7px}
.brand{display:flex;align-items:center;gap:4px;font-size:9px;font-weight:600;letter-spacing:2px}
.brand i{width:22px;height:22px;border:2px solid var(--ink);border-radius:50%;display:block}
.nav .links{margin-left:auto;display:flex;gap:22px}
.nav .icons{display:flex;gap:14px}
.nav .icons b{width:9px;height:10px;background:var(--ink);border-radius:2px;display:block}
.nav .icons u{width:9px;height:9px;border:1.5px solid var(--ink);border-radius:50%;display:block}
.nav.center .brand{margin:0 auto}
.burger{width:10px;height:8px;border-top:1.5px solid var(--ink);border-bottom:1.5px solid var(--ink);position:relative}
.burger::after{content:"";position:absolute;left:0;right:0;top:2px;border-top:1.5px solid var(--ink)}

.hero{height:368px;position:relative}
.hero h1{position:absolute;left:35px;top:140px;font-size:14.5px;line-height:14px;font-weight:700;width:260px}
.hero .rating{position:absolute;left:35px;top:198px;font-size:7px}
.hero .ctas{position:absolute;left:35px;top:212px;display:flex;gap:8px}
.btn{display:inline-flex;align-items:center;justify-content:center;height:28px;padding:0 14px;background:var(--teal);color:#fff;font-size:8px;font-weight:600;border-radius:2px}
.btn.ghost{background:#fff;color:var(--teal);border:1px solid var(--teal)}
.btn.light{background:#fff;color:var(--ink);border-radius:3px}
.btn.black{background:var(--ink);color:#fff;border-radius:3px}
.ring{position:absolute;border-radius:50%}
.r-blue{background:radial-gradient(ellipse at 50% 55%,#fff 0 34%,#1d4fa0 36%,#111 70%)}
.r-gold{background:radial-gradient(ellipse at 50% 50%,#fff 0 30%,#e7c34f 33%,#a7801c 70%)}
.r-black{background:radial-gradient(ellipse at 50% 50%,#fff 0 32%,#444 35%,#111 70%)}
.r-wood{background:radial-gradient(ellipse at 50% 50%,#fff 0 34%,#6b3a1f 37%,#111 60%)}
.r-rose{background:radial-gradient(ellipse at 50% 50%,#fff 0 34%,#e9a577 37%,#222 62%)}
.r-silver{background:radial-gradient(ellipse at 50% 50%,#fff 0 34%,#bbb 37%,#111 62%)}

.collection{height:368px;text-align:center;padding-top:30px}
.collection.dark{background:var(--dark);color:#fff}
.collection.blue{background:var(--blue);color:#fff}
.collection.blush{background:var(--blush)}
.sec-title{font-size:14px;font-weight:700}
.tabs{display:flex;justify-content:center;gap:0;margin-top:18px;font-size:7.5px;font-weight:500}
.tabs span{width:67px;padding-bottom:6px;opacity:.55}
.tabs span.on{opacity:1;font-weight:700;border-bottom:1.5px solid currentColor}
.products{display:flex;justify-content:space-around;padding:0 20px}
.card{width:130px;text-align:center}
.card .img{width:100px;height:100px;margin:0 auto 18px;position:relative}
.card .img .ring{inset:5px 14px}
.card .name{font-size:7px}
.card .price{font-size:9.5px;font-weight:600;margin-top:5px}
.card .btn{margin-top:12px;width:77px;padding:0}
.collection .products{margin-top:40px}
.collection .view{margin-top:50px}

.featured{background:#fff;padding-top:30px}
.featured h2{font-size:14px;font-weight:700;padding-left:29px;display:flex;align-items:center;gap:8px}
.featured h2.teal{color:var(--teal)}
.featured h2.mid{justify-content:center;padding-left:0}
.featured .products{margin-top:20px}
.see-all{text-align:center;color:var(--teal);font-size:8px;font-weight:600;margin-top:30px}
.subtabs{display:flex;justify-content:center;margin-top:16px;font-size:8px;font-weight:600}
.subtabs span{width:113px;text-align:center;padding-bottom:6px;color:var(--teal-light)}
.subtabs span.on{color:var(--teal);border-bottom:1.5px solid var(--teal)}

.engrave{background:var(--grey);position:relative}
.engrave .copy{position:absolute}
.engrave h3{font-size:14px;font-weight:700}
.engrave p{font-size:7px;line-height:8.5px;width:140px;margin:14px 0 16px}

.trust{background:var(--dark);color:#fff;display:flex}
.trust .item{flex:1}
.trust .icon{width:26px;height:26px;background:#fff}
.trust h4{font-size:8.5px;font-weight:700;line-height:10px}
.trust p{font-size:6.5px;line-height:8px;margin-top:8px}
.trust.row{padding:30px 47px 0;gap:14px}
.trust.row .head{display:flex;gap:8px;align-items:flex-start}
.trust.stack{padding:32px 50px 0;text-align:center;gap:20px}
.trust.stack .icon{margin:0 auto 6px}

.reviews{position:relative}
.reviews h2{font-size:14px;font-weight:700;text-align:center}
.reviews h2.teal{color:var(--teal)}
.rv{background:#fff;border-radius:4px;box-shadow:0 1px 6px rgba(0,0,0,.1);position:absolute;font-size:6.5px;line-height:8px}
.rv .who{display:flex;align-items:center;gap:7px;font-weight:600;font-size:7px}
.rv .who i{width:19px;height:19px;border-radius:50%;background:var(--teal);display:block;flex:none}
.rv .stars{font-size:7px;letter-spacing:1px}
.rv .when{color:#aaa}
.rv .thumb{position:absolute}
.arrow{position:absolute;width:22px;height:22px;border-radius:50%;background:#fff;box-shadow:0 1px 4px rgba(0,0,0,.15);display:flex;align-items:center;justify-content:center}
.dots{position:absolute;display:flex;gap:8px}
.dots i{width:6px;height:6px;border-radius:50%;background:#bbb}
.dots i:first-child{background:var(--ink)}

.footer{background:#fff;position:relative}
.footer .brand{position:absolute;left:12px;top:32px}
.fcol{position:absolute;top:32px;font-size:6.5px;line-height:17.5px}
.fcol h5{font-size:8.5px;font-weight:700;line-height:12px;margin-bottom:8px}
.footer .rule{position:absolute;left:12px;right:12px;border-top:1px solid #ccc}
.legal{position:absolute;left:12px;font-size:5.5px;line-height:8px;color:#555}
.pay{position:absolute;right:12px;display:flex;gap:5px}
.pay i{width:16px;height:9px;border-radius:2px;background:#c9d3e0;display:block}
.pay i:nth-child(odd){background:#e3e3e3}
</style>
</head>
<body>
<div class="board">

<!-- Concept A -->
<section class="col col-a" style="height:1737px">
  <div class="topbar"><span>Free Delivery</span><span>Free Returns</span><span>Fast Delivery</span></div>
  <nav class="nav"><div class="brand"><i></i>TORVIKLOOPS</div><div class="links"><span>Shop by Material ⌄</span><span>Shop by Color ⌄</span><span>Try at Home</span></div><div class="icons"><b></b><u></u></div></nav>
  <div class="hero">
    <h1>Elevate Your Style:<br>Handcrafted Rings with Free Fast Delivery &amp; Hassle Free Returns</h1>
    <div class="rating">★★★★★ &nbsp;9,851 Happy Customers</div>
    <div class="ctas"><span class="btn">Shop Now</span></div>
    <div class="ring r-blue" role="img" aria-label="Black and blue tungsten ring" style="left:390px;top:40px;width:126px;height:110px"></div>
    <div class="ring r-gold" role="img" aria-label="Gold domed wedding band" style="left:300px;top:140px;width:88px;height:125px"></div>
    <div class="ring r-black" role="img" aria-label="Black inlay ring" style="left:395px;top:245px;width:124px;height:96px"></div>
  </div>
  <div class="collection dark">
    <div class="sec-title">Bold Steady Iron Collection</div>
    <div class="tabs"><span class="on">BLACK</span><span>SILVER</span><span>BLUE</span><span>GOLD</span><span>BROWN</span><span>ROSE GOLD</span></div>
    <div class="products">
      <div class="card"><div class="img"><div class="ring r-wood" role="img" aria-label="Black ring with wood inlay"></div></div><div class="name">Vanguard</div><div class="price">£48.00</div></div>
      <div class="card"><div class="img"><div class="ring r-rose" role="img" aria-label="Black ring with rose gold inside"></div></div><div class="name">The Craftsman</div><div class="price">£45.00</div></div>
      <div class="card"><div class="img"><div class="ring r-blue" role="img" aria-label="Black and blue ring"></div></div><div class="name">Steadfast</div><div class="price">£45.00</div></div>
      <div class="card"><div class="img"><div class="ring r-silver" role="img" aria-label="Black ring with silver edge"></div></div><div class="name">Resolve</div><div class="price">£46.99</div></div>
    </div>
    <div class="view"><span class="btn light">View All</span></div>
  </div>
  <div class="featured" style="height:302px">
    <h2 class="teal">Top Rated <svg width="14" height="12" viewBox="0 0 14 12"><path d="M1 6h11M7 1l5 5-5 5" stroke="#0e807b" stroke-width="2" fill="none"/></svg></h2>
    <div class="products">
      <div class="card"><div class="img"><div class="ring r-wood" role="img" aria-label="Black ring with wood inlay"></div></div><div class="name">Vanguard</div><div class="price">£48.00</div><span class="btn">Learn More</span></div>
      <div class="card"><div class="img"><div class="ring r-rose" role="img" aria-label="Black ring with rose gold inside"></div></div><div class="name">The Craftsman</div><div class="price">£45.00</div><span class="btn">Learn More</span></div>
      <div class="card"><div class="img"><div class="ring r-blue" role="img" aria-label="Black and blue ring"></div></div><div class="name">Steadfast</div><div class="price">£45.00</div><span class="btn">Learn More</span></div>
      <div class="card"><div class="img"><div class="ring r-silver" role="img" aria-label="Black ring with silver edge"></div></div><div class="name">Resolve</div><div class="price">£46.99</div><span class="btn">Learn More</span></div>
    </div>
  </div>
  <div class="engrave" style="height:226px">
    <div class="ring r-black" role="img" aria-label="Black ring engraved with name and date" style="left:55px;top:40px;width:175px;height:120px"></div>
    <div class="copy" style="left:276px;top:60px"><h3>Personal Ring Engraving</h3><p>Add a personalised engraving to your men's ring. Choose a name, initials, significant date, or short message</p><span class="btn">Make it Yours</span></div>
  </div>
  <div class="reviews" style="height:176px">
    <h2 style="padding-top:28px">Hear From What Our Customers Say</h2>
    <div class="rv" style="left:5px;top:68px;width:160px;height:78px;padding:10px 14px;opacity:.45"><div class="who"><i style="background:#7fc4c0"></i>Owen Hartley</div><div class="stars">★★★★★</div><p style="margin-top:5px">I love the idea of a silicone ring, very clever idea! It is very comfortable to wear and saves the worry of damagin…</p></div>
    <div class="rv" style="left:178px;top:68px;width:208px;height:78px;padding:10px 10px 0 62px"><div class="thumb ring r-gold" role="img" aria-label="Customer photo of gold ring" style="left:16px;top:16px;width:30px;height:42px"></div><div class="who"><i></i>Mia Donnelly</div><div class="stars">★★★★★</div><p style="margin-top:5px">Amazing quality and my fiancé loves it. He wanted a sturdy engagement ring that he can wear whilst he is working…</p></div>
    <div class="rv" style="left:400px;top:68px;width:180px;height:78px;padding:10px 10px 0 62px;opacity:.6"><div class="thumb ring r-rose" role="img" aria-label="Customer photo of rose gold ring" style="left:16px;top:16px;width:34px;height:42px"></div><div class="who"><i></i>Rory Keane</div><div class="stars">★★★★★</div><p style="margin-top:5px">The Ring looks better than the pictures and fitted perfectly</p></div>
  </div>
  <div class="footer" style="height:230px">
    <div class="brand"><i></i>TORVIKLOOPS</div>
    <div class="fcol" style="left:153px"><h5>Important<br>Links</h5>Contact Us<br>Terms of Service<br>Privacy Policy<br>Blog</div>
    <div class="fcol" style="left:238px"><h5>Quick Links</h5>FREE Ring Sizer<br>FREE Delivery<br>Returns and Exchanges<br>Tray at Home<br>Ring Engraving</div>
    <div class="fcol" style="left:347px"><h5>Ring Guide</h5>The Best Tungsten and Titanium Rings<br>How is Tungsten or Titanium Ring Size Measured?<br>The Best Colors for Men Tungsten and Titanium Rings<br>What's Best for Men Tungsten or Titanium</div>
    <div class="rule" style="top:176px"></div>
    <div class="legal" style="top:190px">© 2024 TorvikLoops - 4 Kiln Row, Ashby, AB1 2CD<br>Contact 01000 000000 - hello@torvikloops.com<br>Veldra Ltd - 00000000 - Incorporated on 14 March 2009</div>
    <div class="pay" style="top:200px"><i></i><i></i><i></i><i></i><i></i><i></i><i></i></div>
  </div>
</section>

<!-- Concept B -->
<section class="col col-b" style="height:1944px">
  <div class="topbar"><span>Free Delivery</span><span>Free Returns</span><span>Fast Delivery</span></div>
  <nav class="nav"><div class="brand"><i></i></div><div class="links" style="margin-left:18px"><span>Shop by Material ⌄</span><span>Shop by Color ⌄</span><span>Try at Home</span></div><div class="icons" style="margin-left:auto"><b></b><u></u></div></nav>
  <div class="hero">
    <h1>Elevate Your Style:<br>Handcrafted Rings with Free Fast Delivery &amp; Hassle Free Returns</h1>
    <div class="rating">★★★★★ &nbsp;9,851 Happy Customers</div>
    <div class="ctas"><span class="btn">Discover Our Collections</span></div>
    <div class="ring r-blue" role="img" aria-label="Black and blue tungsten ring" style="left:390px;top:40px;width:126px;height:110px"></div>
    <div class="ring r-gold" role="img" aria-label="Gold domed wedding band" style="left:300px;top:140px;width:88px;height:125px"></div>
    <div class="ring r-black" role="img" aria-label="Black inlay ring" style="left:395px;top:245px;width:124px;height:96px"></div>
  </div>
  <div class="collection blue">
    <div class="sec-title">Bold Steady Iron Collection</div>
    <div class="tabs"><span>BLACK</span><span>SILVER</span><span class="on">BLUE</span><span>GOLD</span><span>BROWN</span><span>ROSE GOLD</span></div>
    <div class="products">
      <div class="card"><div class="img"><div class="ring r-wood" role="img" aria-label="Black ring with wood inlay"></div></div><div class="name">Vanguard</div><div class="price">£48.00</div></div>
      <div class="card"><div class="img"><div class="ring r-rose" role="img" aria-label="Black ring with rose gold inside"></div></div><div class="name">The Craftsman</div><div class="price">£45.00</div></div>
      <div class="card"><div class="img"><div class="ring r-blue" role="img" aria-label="Black and blue ring"></div></div><div class="name">Steadfast</div><div class="price">£45.00</div></div>
      <div class="card"><div class="img"><div class="ring r-silver" role="img" aria-label="Black ring with silver edge"></div></div><div class="name">Resolve</div><div class="price">£46.99</div></div>
    </div>
    <div class="view"><span class="btn light">View All</span></div>
  </div>
  <div class="featured" style="height:332px">
    <h2>Customer Favorites</h2>
    <div class="products">
      <div class="card"><div class="img"><div class="ring r-wood" role="img" aria-label="Black ring with wood inlay"></div></div><div class="name">Vanguard</div><div class="price">£48.00</div><span class="btn">Learn More</span></div>
      <div class="card"><div class="img"><div class="ring r-rose" role="img" aria-label="Black ring with rose gold inside"></div></div><div class="name">The Craftsman</div><div class="price">£45.00</div><span class="btn">Learn More</span></div>
      <div class="card"><div class="img"><div class="ring r-blue" role="img" aria-label="Black and blue ring"></div></div><div class="name">Steadfast</div><div class="price">£45.00</div><span class="btn">Learn More</span></div>
      <div class="card"><div class="img"><div class="ring r-silver" role="img" aria-label="Black ring with silver edge"></div></div><div class="name">Resolve</div><div class="price">£46.99</div><span class="btn">Learn More</span></div>
    </div>
    <div class="see-all">See All →</div>
  </div>
  <div class="engrave" style="height:227px">
    <div class="ring r-black" role="img" aria-label="Black ring engraved with name and date" style="left:55px;top:40px;width:175px;height:120px"></div>
    <div class="copy" style="left:276px;top:60px"><h3>Personal Ring Engraving</h3><p>Add a personalised engraving to your men's ring. Choose a name, initials, significant date, or short message</p><span class="btn">Personalize Your Ring</span></div>
  </div>
  <div class="trust row" style="height:122px">
    <div class="item"><div class="head"><div class="icon"></div><h4>Personal Ring<br>Engraving</h4></div><p>Add a personalised engraving to your men's ring. Choose a name, initials, significant date, or short message</p></div>
    <div class="item"><div class="head"><div class="icon"></div><h4>FREE 1 to 2 Day<br>Delivery &amp; Returns</h4></div><p>FREE One To Two Day Delivery and FREE Returns in case you change your mind (for 100 days)</p></div>
    <div class="item"><div class="head"><div class="icon"></div><h4>Need a<br>Ring Sizer?</h4></div><p>Choose your ring and we'll send you a FREE ring sizer to ensure a perfect fit.</p></div>
  </div>
  <div class="reviews" style="height:253px;background:#f6f6f6">
    <h2 class="teal" style="padding-top:28px">Hear From What Our Customers Say</h2>
    <div class="arrow" style="left:10px;top:108px">‹</div><div class="arrow" style="right:10px;top:108px">›</div>
    <div class="rv" style="left:46px;top:65px;width:148px;height:112px;padding:10px"><div class="who"><i></i><div>Owen Hartley<div class="stars">★★★★★</div></div></div><p style="margin-top:8px;width:82px">I love the idea of a silicone ring, very clever idea! It is very comfortable to wear…</p><p class="when" style="margin-top:18px">yesterday</p><div class="thumb ring r-black" role="img" aria-label="Customer photo of black ring" style="left:100px;top:40px;width:32px;height:38px"></div></div>
    <div class="rv" style="left:207px;top:65px;width:148px;height:112px;padding:10px"><div class="who"><i></i><div>Mia Donnelly<div class="stars">★★★★★</div></div></div><p style="margin-top:8px;width:82px">Amazing quality and my fiancé loves it. He wanted a sturdy engagement ring th…</p><p class="when" style="margin-top:18px">2 days ago</p><div class="thumb ring r-gold" role="img" aria-label="Customer photo of gold ring" style="left:104px;top:40px;width:28px;height:40px"></div></div>
    <div class="rv" style="left:368px;top:65px;width:152px;height:112px;padding:10px"><div class="who"><i></i><div>Rory Keane<div class="stars">★★★★★</div></div></div><p style="margin-top:8px;width:82px">The Ring looks better than the pictures and fitted perfectly</p><p class="when" style="margin-top:26px">3 days ago</p><div class="thumb ring r-rose" role="img" aria-label="Customer photo of rose gold ring" style="left:104px;top:40px;width:34px;height:40px"></div></div>
    <div class="dots" style="left:272px;top:193px"><i></i><i></i></div>
  </div>
  <div class="footer" style="height:208px">
    <div class="brand"><i></i>TORVIKLOOPS</div>
    <div class="fcol" style="left:153px"><h5>Important<br>Links</h5>Contact Us<br>Terms of Service<br>Privacy Policy<br>Blog</div>
    <div class="fcol" style="left:238px"><h5>Quick Links</h5>FREE Ring Sizer<br>FREE Delivery<br>Returns and Exchanges<br>Tray at Home<br>Ring Engraving</div>
    <div class="fcol" style="left:347px"><h5>Ring Guide</h5>The Best Tungsten and Titanium Rings<br>How is Tungsten or Titanium Ring Size Measured?<br>The Best Colors for Men Tungsten and Titanium Rings<br>What's Best for Men Tungsten or Titanium</div>
    <div class="rule" style="top:156px"></div>
    <div class="legal" style="top:170px">© 2024 TorvikLoops - 4 Kiln Row, Ashby, AB1 2CD<br>Contact 01000 000000 - hello@torvikloops.com<br>Veldra Ltd - 00000000 - Incorporated on 14 March 2009</div>
    <div class="pay" style="top:178px"><i></i><i></i><i></i><i></i><i></i><i></i><i></i></div>
  </div>
</section>

<!-- Concept C -->
<section class="col col-c" style="height:2081px">
  <div class="topbar"><span>Free Delivery</span><span>Free Returns</span><span>Fast Delivery</span></div>
  <nav class="nav center"><div class="burger"></div><div class="brand"><i></i>TORVIKLOOPS</div><div class="icons"><b></b><u></u></div></nav>
  <div class="hero">
    <h1>Elevate Your Style:<br>Handcrafted Rings with Free Fast Delivery &amp; Hassle Free Returns</h1>
    <div class="rating">★★★★★ &nbsp;9,851 Happy Customers</div>
    <div class="ctas"><span class="btn">Shop Now</span><span class="btn ghost">Our Collections</span></div>
    <div class="ring r-blue" role="img" aria-label="Black and blue tungsten ring" style="left:390px;top:40px;width:126px;height:110px"></div>
    <div class="ring r-gold" role="img" aria-label="Gold domed wedding band" style="left:300px;top:140px;width:88px;height:125px"></div>
    <div class="ring r-black" role="img" aria-label="Black inlay ring" style="left:395px;top:245px;width:124px;height:96px"></div>
  </div>
  <div class="collection blush">
    <div class="sec-title">Bold Steady Iron Collection</div>
    <div class="tabs"><span>BLACK</span><span>SILVER</span><span>BLUE</span><span>GOLD</span><span>BROWN</span><span class="on">ROSE GOLD</span></div>
    <div class="products">
      <div class="card"><div class="img"><div class="ring r-wood" role="img" aria-label="Black ring with wood inlay"></div></div><div class="name">Vanguard</div><div class="price">£48.00</div></div>
      <div class="card"><div class="img"><div class="ring r-rose" role="img" aria-label="Black ring with rose gold inside"></div></div><div class="name">The Craftsman</div><div class="price">£45.00</div></div>
      <div class="card"><div class="img"><div class="ring r-blue" role="img" aria-label="Black and blue ring"></div></div><div class="name">Steadfast</div><div class="price">£45.00</div></div>
      <div class="card"><div class="img"><div class="ring r-silver" role="img" aria-label="Black ring with silver edge"></div></div><div class="name">Resolve</div><div class="price">£46.99</div></div>
    </div>
    <div class="view"><span class="btn black">View All</span></div>
  </div>
  <div class="featured" style="height:361px">
    <h2 class="mid">UK Best Selling Styles</h2>
    <div class="subtabs"><span class="on">Top Rated</span><span>Customer Favorites</span></div>
    <div class="products">
      <div class="card"><div class="img"><div class="ring r-wood" role="img" aria-label="Black ring with wood inlay"></div></div><div class="name">Vanguard</div><div class="price">£48.00</div><span class="btn">Learn More</span></div>
      <div class="card"><div class="img"><div class="ring r-rose" role="img" aria-label="Black ring with rose gold inside"></div></div><div class="name">The Craftsman</div><div class="price">£45.00</div><span class="btn">Learn More</span></div>
      <div class="card"><div class="img"><div class="ring r-blue" role="img" aria-label="Black and blue ring"></div></div><div class="name">Steadfast</div><div class="price">£45.00</div><span class="btn">Learn More</span></div>
      <div class="card"><div class="img"><div class="ring r-silver" role="img" aria-label="Black ring with silver edge"></div></div><div class="name">Resolve</div><div class="price">£46.99</div><span class="btn">Learn More</span></div>
    </div>
    <div class="see-all">See All →</div>
  </div>
  <div class="engrave" style="height:221px">
    <div class="ring r-blue" role="img" aria-label="Blue and silver ring" style="left:55px;top:20px;width:85px;height:115px"></div>
    <div class="ring r-black" role="img" aria-label="Black ring engraved with name and date" style="left:115px;top:80px;width:125px;height:110px"></div>
    <div class="copy" style="left:289px;top:60px"><h3>Personal Ring Engraving</h3><p>Add a personalised engraving to your men's ring. Choose a name, initials, significant date, or short message</p><span class="btn">Make it Yours</span></div>
  </div>
  <div class="trust stack" style="height:168px">
    <div class="item"><div class="icon"></div><h4>Personal Ring<br>Engraving</h4><p>Add a personalised engraving to your men's ring. Choose a name, initials, significant date, or short message</p></div>
    <div class="item"><div class="icon"></div><h4>FREE 1 to 2 Day<br>Delivery &amp; Returns</h4><p>FREE One To Two Day Delivery and FREE Returns in case you change your mind (for 100 days)</p></div>
    <div class="item"><div class="icon"></div><h4>Need a<br>Ring Sizer?</h4><p>Choose your ring and we'll send you a FREE ring sizer to ensure a perfect fit.</p></div>
  </div>
  <div class="reviews" style="height:264px">
    <h2 class="teal" style="padding-top:28px">Hear From What Our Customers Say</h2>
    <div class="arrow" style="left:24px;top:140px;box-shadow:none">‹</div><div class="arrow" style="right:24px;top:140px;box-shadow:none">›</div>
    <div class="rv" style="left:77px;top:66px;width:125px;height:175px;padding:70px 10px 0"><div class="thumb ring r-black" role="img" aria-label="Customer photo of black ring" style="left:45px;top:14px;width:32px;height:38px"></div><div class="who"><i></i><div>Owen Hartley<div class="stars">★★★★★</div></div></div><p style="margin-top:8px">I love the idea of a silicone ring, very clever idea! It is very comfortable to wear and saves the worry of damagin…</p><p class="when" style="margin-top:12px">yesterday</p></div>
    <div class="rv" style="left:220px;top:66px;width:125px;height:175px;padding:70px 10px 0"><div class="thumb ring r-gold" role="img" aria-label="Customer photo of gold ring" style="left:48px;top:12px;width:28px;height:42px"></div><div class="who"><i></i><div>Mia Donnelly<div class="stars">★★★★★</div></div></div><p style="margin-top:8px">Amazing quality and my fiancé loves it. He wanted a sturdy engagement ring that he can wear whilst he is work…</p><p class="when" style="margin-top:12px">2 days ago</p></div>
    <div class="rv" style="left:363px;top:66px;width:125px;height:175px;padding:70px 10px 0"><div class="thumb ring r-rose" role="img" aria-label="Customer photo of rose gold ring" style="left:45px;top:12px;width:34px;height:42px"></div><div class="who"><i></i><div>Rory Keane<div class="stars">★★★★★</div></div></div><p style="margin-top:8px">The Ring looks better than the pictures and fitted perfectly</p><p class="when" style="margin-top:28px">3 days ago</p></div>
    <div class="dots" style="left:272px;top:258px"><i></i><i></i></div>
  </div>
  <div class="footer" style="height:265px">
    <div class="brand" style="top:50px"><i></i>TORVIKLOOPS</div>
    <div class="fcol" style="left:153px;top:50px"><h5>Important<br>Links</h5>Contact Us<br>Terms of Service<br>Privacy Policy<br>Blog</div>
    <div class="fcol" style="left:238px;top:50px"><h5>Quick Links</h5>FREE Ring Sizer<br>FREE Delivery<br>Returns and Exchanges<br>Tray at Home<br>Ring Engraving</div>
    <div class="fcol" style="left:347px;top:50px"><h5>Ring Guide</h5>The Best Tungsten and Titanium Rings<br>How is Tungsten or Titanium Ring Size Measured?<br>The Best Colors for Men Tungsten and Titanium Rings<br>What's Best for Men Tungsten or Titanium</div>
    <div class="rule" style="top:208px"></div>
    <div class="legal" style="top:222px">© 2024 TorvikLoops - 4 Kiln Row, Ashby, AB1 2CD<br>Contact 01000 000000 - hello@torvikloops.com<br>Veldra Ltd - 00000000 - Incorporated on 14 March 2009</div>
    <div class="pay" style="top:230px"><i></i><i></i><i></i><i></i><i></i><i></i><i></i></div>
  </div>
</section>

</div>
</body>
</html>
```